KerrLow Farm

Need a nice simple clean double sided business card that has our logo and info on:
Kerr Low Farm
Martin & Felicity Kerr Low
kerrlowfarm@mailbarn.example
Martin: 1-780-555-0148
Felicity: 1-780-555-0193
Instagram @ kerrlow_farm

Contact Information for Business Card

Martin & Felicity Kerr Low kerrlowfarm@mailbarn.example Martin: 1-780-555-0148 Felicity: 1-780-555-0193

```html
<!DOCTYPE html>
<html lang="en">
<head>
<meta charset="utf-8">
<title>Kerr Low Farm – Business Card</title>
<link rel="stylesheet" href="https://fonts.googleapis.com/css2?family=Tinos:wght@400&family=Montserrat:wght@500&family=Arimo:wght@400&display=swap">
<style>
  :root {
    --green: #62a01a;
    --green-dark: #558d14;
    --orange: #f6a31b;
    --white: #ffffff;
    --backdrop: #e6e6e3;
    --wheat-soft: #f9d79a;
  }
  * { box-sizing: border-box; margin: 0; padding: 0; }
  html, body { width: 1200px; height: 900px; overflow: hidden; }
  body {
    background: var(--backdrop);
    display: flex;
    flex-direction: column;
    align-items: center;
    justify-content: center;
    gap: 40px;
  }
  .card {
    position: relative;
    width: 700px;
    height: 400px;
    background: var(--white);
    overflow: hidden;
    box-shadow: 0 8px 24px rgba(0,0,0,0.18);
  }

  /* Front */
  .card-front::after {
    content: "";
    position: absolute;
    left: 0; right: 0; bottom: 0;
    height: 8px;
    background: var(--green);
  }
  .wheat-illustration {
    position: absolute;
    left: 20px;
    top: 30px;
    width: 230px;
    height: 362px;
    background: linear-gradient(160deg, var(--orange) 0%, #f8c05a 55%, #8dbb4a 100%);
    border-radius: 40% 40% 8px 8px;
    opacity: 0.85;
  }
  .brand {
    position: absolute;
    display: flex;
    flex-direction: column;
    align-items: center;
  }
  .brand-mark {
    width: 92px;
    height: 92px;
    border: 4px solid var(--green);
    border-radius: 50%;
  }
  .brand-name {
    font-family: "Tinos", serif;
    font-size: 40px;
    color: var(--green);
    letter-spacing: 1px;
    text-transform: uppercase;
    margin-top: 10px;
    white-space: nowrap;
  }
  .brand-tagline {
    font-family: "Montserrat", sans-serif;
    font-weight: 500;
    font-size: 12px;
    color: var(--orange);
    letter-spacing: 7px;
    text-transform: uppercase;
    margin-top: 2px;
  }
  .card-front .brand { left: 280px; top: 90px; width: 390px; }

  /* Back */
  .back-bands { position: absolute; inset: 0; }
  .card-back .brand { left: 0; right: 0; top: 18px; }
  .card-back .brand-mark { width: 80px; height: 80px; }
  .card-back .brand-name { font-size: 34px; margin-top: 8px; }
  .card-back .brand-tagline { font-size: 10px; letter-spacing: 6px; }
  .owners {
    position: absolute;
    left: 190px; width: 370px;
    top: 218px;
    text-align: center;
    font-family: "Tinos", serif;
    font-size: 27px;
    color: var(--orange);
    white-space: nowrap;
  }
  .wheat-faint {
    position: absolute;
    background: linear-gradient(180deg, rgba(255,255,255,0.08), rgba(255,255,255,0.02));
    border-radius: 40% 40% 6px 6px;
  }
  .wheat-faint.left { left: 20px; top: 270px; width: 120px; height: 130px; }
  .wheat-faint.right { right: 10px; top: 250px; width: 110px; height: 150px; }
  .contact {
    position: absolute;
    font-family: "Arimo", sans-serif;
    color: var(--white);
    font-size: 16px;
    line-height: 1.5;
  }
  .contact-phones { left: 160px; top: 300px; }
  .contact-online { right: 40px; top: 300px; text-align: right; }
  .icon-row { display: flex; gap: 8px; margin-bottom: 6px; }
  .contact-online .icon-row { justify-content: flex-end; }
  .icon {
    width: 20px; height: 20px;
    border-radius: 50%;
    background: var(--white);
    display: flex; align-items: center; justify-content: center;
  }
</style>
</head>
<body>

  <section class="card card-front" aria-label="Business card front">
    <div class="wheat-illustration" role="img" aria-label="Illustration of two golden wheat stalks with green leaves"></div>
    <div class="brand">
      <div class="brand-mark"></div>
      <div class="brand-name">Kerr Low Farm</div>
      <div class="brand-tagline">Stone milled flour</div>
    </div>
  </section>

  <section class="card card-back" aria-label="Business card back">
    <svg class="back-bands" width="700" height="400" viewBox="0 0 700 400" aria-hidden="true">
      <polygon points="0,236 180,236 200,262 550,262 570,236 700,236 700,400 0,400" fill="var(--green)"/>
      <polygon points="0,222 180,222 186,230 0,230" fill="var(--orange)"/>
      <polygon points="564,222 700,222 700,230 570,230" fill="var(--orange)"/>
    </svg>
    <div class="wheat-faint left" role="img" aria-label="Faint wheat stalk decoration"></div>
    <div class="wheat-faint right" role="img" aria-label="Faint wheat stalk decoration"></div>

    <div class="brand">
      <div class="brand-mark"></div>
      <div class="brand-name">Kerr Low Farm</div>
      <div class="brand-tagline">Stone milled flour</div>
    </div>

    <div class="owners">Martin &amp; Felicity Kerr Low</div>

    <div class="contact contact-phones">
      <div class="icon-row">
        <span class="icon">
          <svg width="12" height="12" viewBox="0 0 24 24"><path fill="var(--green)" d="M6.6 10.8a15 15 0 0 0 6.6 6.6l2.2-2.2a1 1 0 0 1 1-.25 11.4 11.4 0 0 0 3.6.57 1 1 0 0 1 1 1V20a1 1 0 0 1-1 1A17 17 0 0 1 3 4a1 1 0 0 1 1-1h3.5a1 1 0 0 1 1 1c0 1.25.2 2.45.57 3.6a1 1 0 0 1-.25 1z"/></svg>
        </span>
      </div>
      <div>Martin: 1-780-555-0148</div>
      <div>Felicity: 1-780-555-0193</div>
    </div>

    <div class="contact contact-online">
      <div class="icon-row">
        <span class="icon">
          <svg width="12" height="12" viewBox="0 0 24 24"><rect x="3" y="6" width="18" height="12" rx="1" fill="var(--green)"/><path d="M3 7l9 6 9-6" stroke="var(--white)" stroke-width="1.6" fill="none"/></svg>
        </span>
        <span class="icon"></span>
      </div>
      <div>kerrlowfarm@mailbarn.example</div>
      <div>@ kerrlow_farm</div>
    </div>
  </section>

</body>
</html>
```